A simple Facebook Ad (not Facebook Page) for weight loss surgery

It’s a simple ad in terms of the text.

The text should say:
Curious about weight loss surgery?
This 30 second quiz will tell you which procedure will suit you best

I'm open to variations in the text if it is thought to enhance the ad.

Targeted towards obese individuals who have been unable to lose weight with diet and exercise. My industry is weight loss surgery – webpage www.merivalebardsley.com.au. Clicking the ad leads to a quiz on my webpage relating to weight loss surgery. Most frequent users of this service are females (75%) between ages of 35 and 55 years.

Successful weight loss surgery can enable individuals who have been unable to lose weight to lose a substantial amount of the excess weight they are carrying to be healthier and happier.

```html
<!DOCTYPE html>
<html lang="en">
<head>
<meta charset="utf-8">
<title>Weight Loss Surgery Quiz – Merivale Bardsley</title>
<link rel="stylesheet" href="https://fonts.googleapis.com/css2?family=Bodoni+Moda:wght@400;500&family=Montserrat:wght@500;600&display=swap">
<style>
  :root {
    --paper: #ffffff;
    --ink: #111111;
    --teal: #2f9c97;
    --teal-deep: #1f6f73;
    --band: #4b4b4b;
    --band-text: #ffffff;
    --photo-a: #dcd9d5;
    --photo-b: #7fc4b3;
    --photo-c: #a3a19d;
    --muted: #6b6b6b;
  }
  * { margin: 0; padding: 0; box-sizing: border-box; }
  html, body { width: 1200px; height: 1200px; overflow: hidden; background: var(--paper); }
  .ad { position: relative; width: 1200px; height: 1200px; background: var(--paper); overflow: hidden; }

  .headline { position: relative; z-index: 2; font-family: "Bodoni Moda", "Didot", serif; font-weight: 400; color: var(--ink); line-height: 1; }
  .headline span { position: absolute; white-space: nowrap; }
  .headline .line-1 { left: 89px; top: 58px; font-size: 82px; letter-spacing: 6.5px; }
  .headline .line-2 { left: 156px; top: 160px; font-size: 64px; letter-spacing: 9px; }
  .headline .line-3 { left: 276px; top: 226px; font-size: 92px; }
  .headline .line-4 { left: 488px; top: 312px; font-size: 92px; }

  .question-marks { position: absolute; z-index: 2; font-family: "Montserrat", sans-serif; font-weight: 600; color: var(--teal); line-height: 1; }
  .question-marks.big { left: 952px; top: 130px; font-size: 220px; }
  .question-marks.small { left: 1018px; top: 236px; font-size: 150px; transform: rotate(14deg); }

  .portrait {
    position: absolute; z-index: 1; left: 0; top: 356px; width: 580px; height: 844px;
    background: radial-gradient(ellipse at 45% 40%, var(--photo-b) 0%, var(--photo-b) 30%, transparent 55%),
                linear-gradient(180deg, var(--photo-a) 0%, var(--photo-c) 100%);
    clip-path: polygon(0 0, 470px 0, 580px 70px, 580px 100%, 0 100%);
  }

  .quiz-band { position: absolute; z-index: 2; left: 572px; top: 820px; width: 628px; height: 214px; background: var(--band); }
  .quiz-band .rule { position: absolute; left: 0; right: 0; height: 2px; background: var(--band-text); }
  .quiz-band .rule.top { top: 34px; }
  .quiz-band .rule.bottom { top: 181px; }
  .quiz-copy { position: absolute; left: 0; right: 60px; top: 40px; text-align: center; color: var(--band-text); font-family: "Montserrat", sans-serif; font-weight: 500; letter-spacing: 1.5px; }
  .quiz-copy p { line-height: 1; white-space: nowrap; }
  .quiz-copy .l1 { margin-top: 2px; }
  .quiz-copy .l2, .quiz-copy .l3 { margin-top: 4px; }
  .quiz-copy .big { font-size: 43px; }
  .quiz-copy .small { font-size: 27px; }

  .brand { position: absolute; z-index: 2; left: 664px; top: 1074px; display: flex; align-items: center; gap: 14px; }
  .brand-dot { width: 70px; height: 70px; border-radius: 50%; background: var(--teal); flex: none; }
  .brand-name { font-family: "Bodoni Moda", serif; font-weight: 500; font-size: 28px; color: var(--teal-deep); line-height: 1; white-space: nowrap; }
  .brand-role { font-family: "Bodoni Moda", serif; font-size: 11px; color: var(--muted); letter-spacing: 1.2px; margin-top: 4px; white-space: nowrap; }
</style>
</head>
<body>
<main class="ad">
  <h1 class="headline">
    <span class="line-1">ARE YOU THINKING</span>
    <span class="line-2">ABOUT HAVING A</span>
    <span class="line-3">WEIGHT LOSS</span>
    <span class="line-4">SURGERY</span>
  </h1>
  <div class="question-marks big" aria-hidden="true">?</div>
  <div class="question-marks small" aria-hidden="true">?</div>

  <div class="portrait" role="img" aria-label="Photo of a thoughtful woman in a teal T-shirt and grey trousers sitting on a white block, chin resting on her hand"></div>

  <section class="quiz-band">
    <div class="rule top"></div>
    <div class="rule bottom"></div>
    <div class="quiz-copy">
      <p class="l1"><span class="big">This 30 second quiz</span> <span class="small">will</span></p>
      <p class="l2"><span class="small">tell you which</span> <span class="big">procedure</span></p>
      <p class="l3"><span class="small">will suit you</span> <span class="big">best</span></p>
    </div>
  </section>

  <footer class="brand">
    <div class="brand-dot"></div>
    <div>
      <div class="brand-name">MERIVALE BARDSLEY</div>
      <div class="brand-role">GENERAL, UPPER GI &amp; BARIATRIC SURGEON</div>
    </div>
  </footer>
</main>
</body>
</html>
```